Vellmar Detailing – Premium Automotive Detailing Studio Website Design

We're launching a premium automotive detailing studio called Vellmar Detailing, and we’re looking for a clean, minimal, and high-end website design (desktop + mobile version). The studio targets owners of luxury vehicles who care deeply about aesthetics, perfection, and exceptional service.
This project is about more than just showing services , it should feel like a luxury experience from the very first second. The design should be modern, minimalistic, elegant, and clearly aimed at an upscale market.
We’re looking for a designer who can translate our physical studio’s premium interior and architectural feel into a digital presence.
What we want the website to feel like:
Clean and modern
Professional and luxurious
Minimal and not cluttered
Light animations or transitions to add polish
Stylish and cinematic
Design freedom:
We trust your design direction. We are not providing strict color codes or layout instructions, we want you to create what you believe works best based on our brand positioning and target audience. Just keep it premium, modern, and well-organized.
What the website should include:
Hero section with a bold visual (image or video)
About the Studio — a few blocks explaining our story and focus on quality
Service Overview — clearly showing what we offer (detailing, ceramic coating, interior, etc.)
Gallery/Showcase — show off our work with cars, interior, and the space itself
Client Lounge Area — mention comfort, coffee, and waiting space
Testimonials — social proof from satisfied clients
Location & contact section — map, address, contact form
Footer, simple with nav, contact info, and optional social media
Target audience:
Owners of high-end vehicles (Torvani, Kellard, etc.)
Car collectors and detailing enthusiasts
People looking for premium-level service and presentation
Brands/creators booking our photo studio

```html
<!DOCTYPE html>
<html lang="en">
<head>
<meta charset="utf-8">
<title>Vellmar Detailing – Premium Automotive Detailing Studio</title>
<link href="https://fonts.googleapis.com/css2?family=Archivo:wght@400;600;700;800&family=Poppins:wght@400;500;600&display=swap" rel="stylesheet">
<style>
:root{
  --gold:#b9a15e;
  --gold-dark:#8f7b44;
  --black:#000;
  --card:#111111;
  --white:#fff;
  --head:"Archivo",sans-serif;
  --body:"Poppins",sans-serif;
}
*{box-sizing:border-box;margin:0;padding:0}
html,body{width:1200px;height:4320px;overflow:hidden;background:var(--black)}
body{position:relative;font-family:var(--body);color:var(--white)}
.abs{position:absolute}
.section{position:absolute;left:0;width:1200px;overflow:hidden}
.fill{position:absolute}
.eyebrow{font-family:var(--body);font-size:14px;font-weight:500;color:var(--gold);white-space:nowrap}
.ghost{font-family:var(--head);font-weight:800;font-size:52px;color:transparent;-webkit-text-stroke:1px rgba(255,255,255,.12);letter-spacing:1px;line-height:1;white-space:nowrap}
.title{font-family:var(--head);font-weight:700;text-transform:uppercase;line-height:1.2;white-space:nowrap}
.btn{position:absolute;display:flex;align-items:center;justify-content:center;font-family:var(--head);font-weight:700;font-size:14px;text-transform:uppercase;letter-spacing:.3px;white-space:nowrap}
.btn-gold{background:var(--gold);color:#111}
.btn-dark{background:#000;color:var(--white)}
.wordmark{font-family:var(--head);font-weight:700;color:var(--white);line-height:1;display:flex;align-items:center;gap:10px}
.wordmark .mark{width:26px;height:26px;border:2px solid var(--white);flex:none}

/* header */
.header{top:0;height:88px;background:#050505}
.topbar{position:absolute;top:0;left:652px;width:402px;height:30px;display:flex;font-size:12px}
.topbar div{display:flex;align-items:center;justify-content:center;gap:8px}
.topbar .phone{width:175px;background:var(--gold-dark);color:#fff}
.topbar .mail{flex:1;background:#c9c9c9;color:#333}
.nav{position:absolute;top:54px;left:416px;display:flex;gap:48px;font-family:var(--head);font-size:13px;font-weight:600}
.nav a{color:var(--white);text-decoration:none}
.nav a.active{color:var(--gold)}

/* hero */
.hero{top:88px;height:574px}
.hero .photo{inset:0;background:linear-gradient(180deg,#5b5546 0%,#2a261f 45%,#16130e 100%)}
.hero .car{left:520px;top:120px;width:640px;height:360px;border-radius:50% 50% 12% 12%/60% 60% 12% 12%;background:radial-gradient(ellipse at 50% 55%,#3d3d3b 0%,#1c1c1b 45%,rgba(20,18,14,0) 75%)}
.hero .shade{inset:0;background:linear-gradient(90deg,rgba(0,0,0,.45) 0%,rgba(0,0,0,.1) 50%,rgba(0,0,0,0) 100%)}
.hero h1{position:absolute;left:144px;top:172px;font-size:37px;line-height:56px;font-family:var(--head);font-weight:700;text-transform:uppercase;white-space:nowrap}
.rating{position:absolute;left:144px;top:488px;display:flex;align-items:center;gap:18px}
.avatars{display:flex}
.avatars span{width:36px;height:36px;border-radius:50%;background:#6d6253;border:2px solid #ddd;margin-left:-10px}
.avatars span:first-child{margin-left:0}
.rating .score{font-family:var(--head);font-size:36px;font-weight:700}
.rating small{display:block;font-size:11px;letter-spacing:1.5px}
.stars{color:var(--gold);font-size:13px;letter-spacing:2px}
.dots{position:absolute;left:580px;top:527px;display:flex;gap:5px}
.dots i{width:9px;height:9px;border:1px solid #ddd;display:block}
.dots i.on{background:var(--gold);border-color:var(--gold)}
.scroll{position:absolute;left:1160px;top:420px;writing-mode:vertical-rl;font-size:10px;letter-spacing:2px}
.scroll::before{content:"";position:absolute;left:4px;top:-90px;width:1px;height:80px;background:var(--gold)}

/* about + lounge */
.about{top:662px;height:568px;background:var(--black)}
.about p{position:absolute;left:144px;width:410px;font-size:12.5px;line-height:24px;color:#e8e8e8}

/* services */
.services{top:1230px;height:775px;background:var(--gold)}
.services .title{color:#111;font-size:34px;line-height:48px}
.services .ghost{-webkit-text-stroke:0;color:rgba(0,0,0,.18)}
.circle-btn{position:absolute;width:58px;height:58px;border:1.5px solid #111;border-radius:50%;display:flex;flex-direction:column;align-items:center;justify-content:center;font-size:10px;color:#111;font-weight:600}
.tile{position:absolute;width:296px;height:320px;overflow:hidden}
.tile .img{position:absolute;inset:0}
.tile .label{position:absolute;left:0;right:0;bottom:38px;text-align:center;font-size:16px;font-weight:500}
.tile .chev{position:absolute;left:0;right:0;bottom:14px;text-align:center;font-size:12px}
.tile.feature .img{background:#e7e7e7}
.tile.feature .inner{position:absolute;inset:0;display:flex;flex-direction:column;align-items:center;padding:34px 20px 0;color:#222;text-align:center}
.tile.feature h3{font-weight:500;font-size:16px;margin:10px 0 16px}
.tile.feature p{font-size:12px;line-height:22px;color:#444}
.tile.feature .outline{margin-top:14px;border:1.5px solid #222;width:140px;height:40px;display:flex;align-items:center;justify-content:center;font-family:var(--head);font-weight:700;font-size:13px}

/* testimonials */
.testimonials{top:2005px;height:530px;background:#050505}
.arrow{position:absolute;width:36px;height:36px;border-radius:50%;display:flex;align-items:center;justify-content:center}
.tcard{position:absolute;top:204px;width:216px;height:278px;background:var(--card);padding:22px 22px}
.tcard .q{font-family:var(--head);font-size:44px;color:var(--gold);line-height:.7;height:36px}
.tcard p{font-size:12.5px;line-height:24px;color:#ddd;margin-top:6px}
.tcard .who{position:absolute;left:22px;bottom:22px;display:flex;gap:14px;align-items:center}
.tcard .face{width:50px;height:50px;border-radius:50%;background:#5a5148}
.tcard strong{font-size:14px;font-weight:600;display:block}
.social{display:flex;gap:7px;margin-top:4px}
.social i{width:9px;height:9px;border-radius:50%;background:var(--gold);display:block}

/* gallery */
.gallery{top:2535px;height:599px;background:#000}
.shot{position:absolute}

/* appointment */
.appointment{top:3134px;height:314px;background:var(--gold);text-align:center;color:#111}

/* contact */
.contact{top:3448px;height:566px;background:#050505}
.field{position:absolute;width:262px;border-bottom:1px solid #888;height:34px;font-size:12px;display:flex;align-items:flex-start;gap:8px}
.field svg{flex:none;margin-top:2px}

/* footer */
.footer{top:4014px;height:306px;background:#000}
.col h4{font-family:var(--head);font-size:14px;font-weight:600;color:var(--gold);margin-bottom:10px}
.col li{list-style:none;font-size:13px;line-height:21px;display:flex;gap:12px}
.col li::before{content:"»";color:var(--gold)}
.contact-list div{display:flex;gap:12px;align-items:flex-start;font-size:12.5px;line-height:18px;margin-bottom:14px;width:250px}
.contact-list .ic{width:24px;height:24px;border:1.5px solid #ccc;border-radius:50%;flex:none}
</style>
</head>
<body>

<header class="section header">
  <div class="abs wordmark" style="left:144px;top:24px;font-size:24px;letter-spacing:2px">
    <span class="mark"></span><span>VELLMAR<br><span style="font-size:13px;letter-spacing:6px">DETAILING</span></span>
  </div>
  <div class="topbar">
    <div class="phone"><svg width="11" height="11" viewBox="0 0 24 24" fill="#fff"><path d="M6.6 10.8a15 15 0 006.6 6.6l2.2-2.2a1 1 0 011-.25 11.4 11.4 0 003.6.57 1 1 0 011 1V20a1 1 0 01-1 1A17 17 0 013 4a1 1 0 011-1h3.5a1 1 0 011 1c0 1.25.2 2.45.57 3.6a1 1 0 01-.25 1z"/></svg>+1-555-010-2040</div>
    <div class="mail"><svg width="12" height="10" viewBox="0 0 24 18" fill="#333"><rect width="24" height="18" rx="2"/></svg>info@vellmardetailing.com</div>
  </div>
  <nav class="nav">
    <a class="active">HOME</a><a>ABOUT US</a><a>SERVICES</a><a>GALLERY</a><a>LOCATION</a><a>CONTACT US</a>
  </nav>
</header>

<section class="section hero">
  <div class="fill photo"></div>
  <div class="fill car" role="img" aria-label="Matte black Torvani sports car on a warm, dusky road"></div>
  <div class="fill shade"></div>
  <div class="eyebrow abs" style="left:144px;top:148px;font-size:13px">WELCOME TO VELLMAR DETAILING,</div>
  <h1>Pamper your car.<br>Elevate your drive.</h1>
  <div class="btn btn-gold" style="left:144px;top:314px;width:243px;height:50px">Make an appointment</div>
  <div class="rating">
    <div class="avatars" role="img" aria-label="Client portraits"><span></span><span></span><span></span></div>
    <div class="score">5.0</div>
    <div><div class="stars">★★★★★</div><small>5.2K Reviews</small></div>
  </div>
  <div class="dots"><i></i><i class="on"></i><i></i></div>
  <div class="scroll">SCROLL DOWN ›</div>
</section>

<section class="section about">
  <div class="ghost abs" style="left:144px;top:110px">WHO</div>
  <div class="eyebrow abs" style="left:256px;top:128px">We Are</div>
  <h2 class="title abs" style="left:144px;top:174px;font-size:30px">About Vellmar Detailing</h2>
  <p style="top:226px">Lorem ipsum dolor sit amet, consectetur adipiscing elit, sed do eiusmod tempor incididunt ut labore et dolore magna aliqua. Ut enim ad minim veniam, quis nostrud exercitation ullamco laboris nisi ut aliquip ex ea commodo consequat.</p>
  <p style="top:328px">Our client lounge offers comfort while you wait: fresh coffee, soft seating and a quiet view of the studio floor.</p>
  <div class="btn btn-gold" style="left:144px;top:412px;width:143px;height:42px">Read more</div>
  <svg class="abs" style="left:626px;top:48px" width="48" height="44"><g fill="#bbb"><circle cx="2" cy="2" r="1.5"/><circle cx="14" cy="2" r="1.5"/><circle cx="26" cy="2" r="1.5"/><circle cx="38" cy="2" r="1.5"/><circle cx="2" cy="14" r="1.5"/><circle cx="14" cy="14" r="1.5"/><circle cx="2" cy="26" r="1.5"/><circle cx="2" cy="38" r="1.5"/></g></svg>
  <svg class="abs" style="left:634px;top:90px" width="450" height="432"><polygon points="440,20 440,425 40,425 60,405 420,405 420,40" fill="#b9a15e"/><polygon points="0,120 15,110 15,400 0,410" fill="#444"/></svg>
  <div class="fill" style="left:649px;top:72px;width:407px;height:401px;background:linear-gradient(135deg,#2b2b2b,#5a1418 55%,#1a1a1a)" role="img" aria-label="Detailer in black gloves polishing a red car headlight"></div>
</section>

<section class="section services">
  <div class="ghost abs" style="left:144px;top:70px">WHAT</div>
  <div class="abs" style="left:276px;top:84px;font-size:14px;font-weight:500;color:#111">We Do</div>
  <h2 class="title abs" style="left:142px;top:136px">Experience<br>Our services<br>Excellence</h2>
  <div class="circle-btn" style="left:144px;top:294px">PREV<span>‹</span></div>
  <div class="circle-btn" style="left:212px;top:294px">NEXT<span>›</span></div>

  <div class="tile" style="left:452px;top:59px"><div class="img" style="background:linear-gradient(160deg,#3a3a3a,#111)" role="img" aria-label="Foamed car headlight during clay bar treatment"></div><div class="label">Clay Bar Treatment</div><div class="chev">⌃</div></div>
  <div class="tile" style="left:759px;top:59px"><div class="img" style="background:linear-gradient(160deg,#6b6b6b,#1c1c1c)" role="img" aria-label="Polishing machine applying ceramic coating"></div><div class="label">Ceramic Coating</div><div class="chev">⌃</div></div>
  <div class="tile" style="left:146px;top:389px"><div class="img" style="background:linear-gradient(160deg,#4a4a4a,#151515)" role="img" aria-label="Vacuum removing pet hair from seat"></div><div class="label">Pet Hair Removal</div><div class="chev">⌃</div></div>
  <div class="tile feature" style="left:452px;top:389px"><div class="img" role="img" aria-label="Faint detailing background"></div>
    <div class="inner">
      <svg width="70" height="60" viewBox="0 0 70 60" fill="none" stroke="#222" stroke-width="2.5"><path d="M12 40 L18 26 H52 L58 40 Z"/><rect x="8" y="40" width="54" height="12" rx="3"/><circle cx="18" cy="46" r="3"/><circle cx="52" cy="46" r="3"/><circle cx="48" cy="12" r="7"/><path d="M48 5 v-3 M48 19 v3 M41 12 h-3 M55 12 h3"/></svg>
      <h3>Detailing</h3>
      <p>Sed ut perspiciatis unde omnis iste natus error sit voluptatem accusantium doloremque laudantium, totam rem</p>
      <div class="outline">READ MORE</div>
    </div></div>
  <div class="tile" style="left:759px;top:389px"><div class="img" style="background:linear-gradient(160deg,#5a5a5a,#101010 60%,#6e6232)" role="img" aria-label="Gloved hand wiping car with yellow microfiber"></div><div class="label">Interior</div><div class="chev">⌃</div></div>
</section>

<section class="section testimonials">
  <div class="ghost abs" style="left:144px;top:62px">CLIENT</div>
  <div class="eyebrow abs" style="left:296px;top:80px">Satisfaction</div>
  <h2 class="title abs" style="left:144px;top:128px;font-size:32px">Real stories, real success</h2>
  <div class="arrow" style="left:971px;top:123px;background:#fff"><svg width="14" height="14" viewBox="0 0 14 14"><path d="M13 7H2M6 2L1 7l5 5" stroke="#111" stroke-width="2" fill="none"/></svg></div>
  <div class="arrow" style="left:1017px;top:123px;background:var(--gold)"><svg width="14" height="14" viewBox="0 0 14 14"><path d="M1 7h11M8 2l5 5-5 5" stroke="#111" stroke-width="2" fill="none"/></svg></div>

  <div class="tcard" style="left:144px"><div class="q">“</div><p>Lorem ipsum dolor sit amet, consectetur adipiscing elit, sed do eiusmod tempor incididunt ut labore et dolore magna</p><div class="who"><div class="face" role="img" aria-label="Client portrait"></div><div><strong>Harlan M</strong><div class="social"><i></i><i></i><i></i></div></div></div></div>
  <div class="tcard" style="left:375px"><div class="q">“</div><p>Lorem ipsum dolor sit amet, consectetur adipiscing elit, sed do eiusmod tempor incididunt ut labore et dolore magna</p><div class="who"><div class="face" role="img" aria-label="Client portrait"></div><div><strong>Brennick K</strong><div class="social"><i></i><i></i><i></i></div></div></div></div>
  <div class="tcard" style="left:607px"><div class="q">“</div><p>Lorem ipsum dolor sit amet, consectetur adipiscing elit, sed do eiusmod tempor incididunt ut labore et dolore magna</p><div class="who"><div class="face" role="img" aria-label="Client portrait"></div><div><strong>Talia S</strong><div class="social"><i></i><i></i><i></i></div></div></div></div>
  <div class="tcard" style="left:838px"><div class="q">“</div><p>Lorem ipsum dolor sit amet, consectetur adipiscing elit, sed do eiusmod tempor incididunt ut labore et dolore magna</p><div class="who"><div class="face" role="img" aria-label="Client portrait"></div><div><strong>Corvin N</strong><div class="social"><i></i><i></i><i></i></div></div></div></div>
</section>

<section class="section gallery">
  <div class="ghost abs" style="left:540px;top:30px">OUR</div>
  <div class="eyebrow abs" style="left:639px;top:42px">Gallery</div>
  <h2 class="title abs" style="left:0;width:1200px;text-align:center;top:92px;font-size:32px">Completed projects</h2>
  <div class="shot" style="left:0;top:177px;width:193px;height:261px;background:linear-gradient(90deg,#0a0a0a,#222)" role="img" aria-label="Dark car detail, faded"></div>
  <div class="shot" style="left:204px;top:177px;width:220px;height:261px;background:linear-gradient(160deg,#d8d8d8,#7a2a20 60%,#333)" role="img" aria-label="Detailer in mask working on a red car"></div>
  <div class="shot" style="left:439px;top:165px;width:320px;height:285px;background:linear-gradient(150deg,#1a1a1a,#4a4a4a 55%,#0d0d0d)" role="img" aria-label="Gloved hand applying coating to black car"></div>
  <div class="shot" style="left:774px;top:177px;width:220px;height:261px;background:linear-gradient(160deg,#3b4e7a,#2a2a2a 60%,#c5c5c5)" role="img" aria-label="Detailer polishing car with cloth"></div>
  <div class="shot" style="left:1009px;top:177px;width:191px;height:261px;background:linear-gradient(270deg,#0a0a0a,#222)" role="img" aria-label="Dark car detail, faded"></div>
  <div class="arrow" style="left:294px;top:478px;width:46px;height:46px;border:1.5px solid #fff;color:#fff">‹</div>
  <div class="arrow" style="left:350px;top:482px;width:38px;height:38px;border:1.5px solid var(--gold);color:var(--gold)">›</div>
  <div class="abs" style="left:422px;top:500px;width:416px;height:2px;background:#222"></div>
  <div class="abs" style="left:422px;top:499px;width:120px;height:4px;background:var(--gold)"></div>
  <div class="abs title" style="left:842px;top:486px;font-size:20px;letter-spacing:8px"><span style="color:var(--gold)">1</span>23</div>
</section>

<section class="section appointment">
  <div class="ghost abs" style="left:488px;top:38px;-webkit-text-stroke:0;color:rgba(0,0,0,.15)">IN NEED</div>
  <div class="abs" style="left:676px;top:56px;font-size:14px;font-weight:500">of Services</div>
  <h2 class="title abs" style="left:0;width:1200px;top:108px;font-size:32px">Schedule online appointment</h2>
  <div class="abs" style="left:0;width:1200px;top:162px;font-size:15px;color:#222">Lorem Ipsum Dolor Sit Amet, Consectetur Adipiscing Elit, Sed Do Eiusmod Tempor Incididunt.</div>
  <div class="btn btn-dark" style="left:486px;top:211px;width:226px;height:43px">Make an appointment</div>
</section>

<section class="section contact">
  <div class="fill" style="left:0;top:50px;width:431px;height:476px;background:#ececec" role="img" aria-label="Street map showing studio location"></div>
  <svg class="abs" style="left:206px;top:232px" width="56" height="72" viewBox="0 0 56 72"><path d="M28 0C12 0 0 12 0 27c0 20 28 45 28 45s28-25 28-45C56 12 44 0 28 0z" fill="#b9a15e"/><circle cx="28" cy="27" r="11" fill="#fff"/></svg>
  <div class="ghost abs" style="left:493px;top:94px">GET</div>
  <div class="eyebrow abs" style="left:580px;top:112px">In Touch</div>
  <h2 class="title abs" style="left:493px;top:146px;font-size:32px">Contact us today</h2>
  <div class="field" style="left:496px;top:204px"><svg width="10" height="11" viewBox="0 0 10 11" fill="#fff"><circle cx="5" cy="3" r="3"/><path d="M0 11c0-3 2-5 5-5s5 2 5 5z"/></svg>First Name</div>
  <div class="field" style="left:793px;top:204px"><svg width="10" height="11" viewBox="0 0 10 11" fill="#fff"><circle cx="5" cy="3" r="3"/><path d="M0 11c0-3 2-5 5-5s5 2 5 5z"/></svg>Last Name</div>
  <div class="field" style="left:496px;top:273px"><svg width="12" height="9" viewBox="0 0 12 9" fill="#fff"><rect width="12" height="9" rx="1"/></svg>Email Address</div>
  <div class="field" style="left:793px;top:273px"><svg width="11" height="11" viewBox="0 0 24 24" fill="#fff"><path d="M6.6 10.8a15 15 0 006.6 6.6l2.2-2.2a1 1 0 011-.25 11.4 11.4 0 003.6.57 1 1 0 011 1V20a1 1 0 01-1 1A17 17 0 013 4a1 1 0 011-1h3.5a1 1 0 011 1c0 1.25.2 2.45.57 3.6a1 1 0 01-.25 1z"/></svg>Phone Number</div>
  <div class="field" style="left:496px;top:342px;width:558px;height:72px"><svg width="12" height="10" viewBox="0 0 12 10" fill="#fff"><ellipse cx="6" cy="4.5" rx="6" ry="4.5"/></svg>Message</div>
  <div class="btn btn-gold" style="left:496px;top:454px;width:144px;height:42px">Submit now</div>
</section>

<footer class="section footer">
  <div class="abs" style="left:144px;top:52px;width:170px;display:flex;flex-direction:column;align-items:center;font-family:var(--head);font-weight:700;line-height:1">
    <span style="width:56px;height:56px;border:3px solid #fff;margin-bottom:16px"></span>
    <span style="font-size:30px;letter-spacing:2px">VELLMAR</span>
    <span style="font-size:16px;letter-spacing:8px;margin-top:6px">DETAILING</span>
  </div>
  <div class="col abs" style="left:390px;top:56px"><h4>QUICK LINKS</h4><ul><li>Home</li><li>About Us</li><li>Services</li><li>Gallery</li><li>Location</li><li>Contact Us</li></ul></div>
  <div class="col abs" style="left:585px;top:56px"><h4>OTHER LINKS</h4><ul><li>Careers</li><li>Customer Service</li><li>Gift Cards</li><li>Site Map</li><li>Privacy Policy</li><li>Terms of Services</li></ul></div>
  <div class="col abs contact-list" style="left:811px;top:56px"><h4>CONTACT US</h4>
    <div><span class="ic"></span>+1-555-010-2040</div>
    <div><span class="ic"></span>hello@vellmarstudio.com</div>
    <div><span class="ic"></span>10 Duis aute irure dolor in reprehen derit in voluptate 5263,AUS</div>
    <div><span class="ic"></span>Mon To Sat: 8.00 AM To 9 PM</div>
  </div>
  <div class="abs" style="left:144px;top:253px;width:912px;height:1px;background:#333"></div>
  <div class="abs" style="left:0;width:1200px;top:264px;text-align:center;font-size:12px">© 2025 Vellmar Detailing &nbsp;|&nbsp; All Rights Reserved</div>
</footer>

</body>
</html>
```